サイト構成・基本的な要件については
https://drawlumo.com/boards/R3TX9pamqzeh2WnL
を併せてご覧いただければ幸いです。
※導線が確保されていれば、必ずしもレイアウト案に忠実である必要はございません。
ぜひご提案いただければ幸甚です。

また、素材については
http://parcelvault.jp/get/91a7c2e05d4f18b6a3c29e7d10f5b84a2e6c90d3
よりダウンロードいただければと存じます。

上記だけで制作が難しい場合は
http://fotomoru.jp/
などから、5000円程度までならこちらにて購入可能です。カンプデータにて作成頂き、
納品時に当方にて購入したデータに差し替えていただければと存じます。

全体的なデザインのイメージとしては

http://www.plumrow-garden.jp/
http://www.tavolix.co.jp/bitemode/
http://verdalio.jp/
http://yu-morikawa.com/
のような、白ベースですっきりと見やすい印象が希望です。

メインカラーは既存サイトと同様、グリーンでお願いします。
http://www.sakuradaplate.co.jp/
1ページ
白を基調とし、グリーンベースでスッキリと明るく見やすいデザインを希望します
素材については
よりダウンロードいただければと存じます。

上記だけで制作が難しい場合は
http://fotomoru.jp/

白ベースでメインカラーは既存と同様にグリーンを使用し、
明るく見やすいデザインをお願いできればと思います。

http://baseline-gallery.com/2012/208.html
http://baseline-gallery.com/2011/143.html
→フッター部分の参照

基本レイアウト
については、必ずしも忠実である必要はありません。

是非ご提案お待ちしております。
何卒よろしくお願いいたします。

制作につきましてご不明な点がございましたら、お気軽にお申し付けいただければと存じます。
ご提案お待ちしております。

クライアント様との協議の結果こちらの案を採用させていただきました。
高級感と柔らかさのバランスがとてもよく、
視認性も高く、要望を全て満たしておりましたので
こちらの案を採用いたしました。

この度は多数ご提案いただきありがとうございました。
当選に至らなかったランサー様におかれましては大変心苦しいのですが、
またの機会にぜひご提案いただければ幸甚です。
引き続き何卒よろしくお願いいたします。

```html
<!DOCTYPE html>
<html lang="ja">
<head>
<meta charset="utf-8">
<title>桜田クッキング</title>
<link href="https://fonts.googleapis.com/css2?family=Noto+Sans+JP:wght@400;700&family=Kosugi+Maru&family=Kaushan+Script&family=Yusei+Magic&display=swap" rel="stylesheet">
<style>
:root{
  --green:#78b534;
  --green-dark:#4f8f1c;
  --green-pale:#eef6e2;
  --yellow:#f4de3c;
  --yellow-pale:#fdf6c6;
  --orange:#ef8a2a;
  --text:#4a4a4a;
  --muted:#8c8c8c;
  --line:#dcdcdc;
}
*{box-sizing:border-box;margin:0;padding:0}
html,body{width:1200px;height:2888px;overflow:hidden}
body{position:relative;background:#fff;color:var(--text);font-family:"Noto Sans JP",sans-serif;font-size:14px;line-height:1.6}
a{color:inherit;text-decoration:none}
.abs{position:absolute}

/* header */
.brand{left:70px;top:24px;display:flex;align-items:center;gap:12px}
.brand-mark{width:46px;height:46px;border-radius:50%;background:var(--green)}
.brand-name{font-family:"Kosugi Maru",sans-serif;font-size:30px;color:var(--green-dark);line-height:1.1}
.brand-sub{font-size:12px;color:var(--green-dark);letter-spacing:.05em}
.util{right:70px;top:20px;display:flex;gap:22px;font-size:12px;color:var(--muted)}
.util span::before{content:"▸ ";color:var(--green)}
.reserve{right:70px;top:52px;background:var(--green);color:#fff;font-size:13px;padding:6px 22px;border-radius:16px}

.gnav{left:70px;top:118px;width:1060px;height:70px;display:flex;border-top:1px solid var(--line);border-bottom:3px solid var(--green)}
.gnav a{flex:1;min-width:0;display:flex;flex-direction:column;align-items:center;justify-content:center;font-size:13px;font-weight:700;color:var(--text);border-right:1px dotted var(--line);white-space:nowrap;letter-spacing:-.02em}
.gnav a small{font-size:9px;font-weight:400;color:var(--muted);letter-spacing:.08em}
.gnav a.active{background:var(--yellow)}

/* hero */
.hero{left:70px;top:200px;width:1060px;height:420px;background:linear-gradient(100deg,#f4f6ee 0%,#f1ead8 35%,#e9dcc4 60%,#d9c6a8 100%)}
.hero-veg{left:70px;top:420px;width:400px;height:200px;background:linear-gradient(90deg,#c94a2c 0%,#e2a93a 35%,#7aa83a 70%,#eef0e4 100%);opacity:.85}
.hero-copy{left:110px;top:236px}
.hero-copy h1{font-family:"Yusei Magic",sans-serif;font-size:42px;color:var(--green);font-weight:400;line-height:1.2}
.hero-copy p{font-size:14px;color:var(--text);margin-top:12px;line-height:1.8}
.hero-more{left:110px;top:382px;background:var(--green);color:#fff;font-size:12px;padding:4px 20px;border-radius:12px}
.dots{left:1050px;top:630px;display:flex;gap:8px}
.dots i{width:10px;height:10px;border-radius:50%;background:var(--line)}
.dots i:first-child{background:var(--green)}

/* sidebar */
.trial{left:70px;top:672px;width:250px;height:410px;border:2px solid var(--green);border-radius:6px;background:#fff;padding:18px}
.trial-icon{width:60px;height:40px;margin:0 auto 8px;display:block}
.trial h2{font-size:24px;color:var(--green-dark);font-weight:700;line-height:1.3}
.trial .badge{position:absolute;right:14px;top:80px;width:60px;height:60px;border-radius:50%;background:var(--yellow);font-size:12px;font-weight:700;display:flex;align-items:center;justify-content:center;text-align:center;line-height:1.2}
.trial .lead{font-size:12px;margin:10px 0 12px}
.tel{display:flex;align-items:center;gap:8px;margin-bottom:10px}
.tel b{background:var(--green);color:#fff;font-size:11px;padding:3px 7px;border-radius:3px}
.tel span{font-size:20px;font-weight:700;color:var(--green-dark);letter-spacing:.02em}
.side-nav{left:70px;top:1135px;width:250px;list-style:none;border-top:1px dotted var(--line)}
.side-nav li{height:55px;line-height:55px;border-bottom:1px dotted var(--line);font-size:14px;padding-left:8px}
.side-nav li::before{content:"▸ ";color:var(--green)}
.corp{left:70px;top:1590px;width:250px;height:150px;background:var(--yellow-pale);border:2px solid var(--yellow);padding:18px;text-align:center}
.corp h3{font-size:17px;color:var(--text)}
.corp p{font-size:12px;margin-top:8px;color:var(--muted)}

/* main */
.sec-head{display:flex;align-items:center;gap:14px;border-bottom:2px dotted var(--green);padding-bottom:6px}
.sec-head h2{font-family:"Kaushan Script",cursive;font-weight:400;font-size:34px;color:var(--green)}
.sec-head h2.jp{font-family:"Yusei Magic",sans-serif;font-size:28px}
.sec-head small{font-size:12px;color:var(--muted)}
.news{left:360px;top:665px;width:770px}
.news-item{display:flex;gap:16px;padding:18px 0;border-bottom:1px dotted var(--line);font-size:13px}
.news-item time{color:var(--green-dark);font-weight:700;white-space:nowrap}
.new{display:inline-block;background:var(--orange);color:#fff;font-size:10px;padding:0 6px;border-radius:2px;margin-top:4px}
.news-item p{line-height:1.7}

.menu{left:360px;top:1030px;width:770px}
.menu-item{display:flex;gap:24px;padding:22px 0;border-bottom:1px dotted var(--line)}
.photo{flex:none}
.menu-item .photo{width:180px;height:130px;border-radius:4px}
.menu-item h3{font-size:13px;color:var(--green-dark);margin-bottom:6px}
.menu-item h3 span{color:var(--orange);margin-left:8px}
.menu-item p{font-size:13px}
.more{display:block;text-align:right;font-size:12px;color:var(--muted);margin-top:10px}
.more::before{content:"● ";color:var(--green);font-size:10px}

.about{left:360px;top:1680px;width:770px}
.about-title{display:flex;align-items:center;gap:20px}
.about-title::before,.about-title::after{content:"";flex:1;border-top:2px dotted var(--green)}
.about-title h2{font-family:"Yusei Magic",sans-serif;font-weight:400;font-size:32px;color:var(--green)}
.about-lead{text-align:center;font-size:13px;color:var(--muted);margin:14px 0 26px}
.cards{display:grid;grid-template-columns:repeat(3,240px);gap:34px 25px}
.card{border:1px solid var(--line);background:#fff}
.card .photo{height:190px}
.card-body{padding:12px 16px;height:150px;position:relative}
.card h3{font-size:17px;color:var(--green-dark);text-align:center;margin-bottom:6px}
.card p{font-size:12px;line-height:1.7}
.card .go{position:absolute;left:16px;bottom:12px;font-size:11px;color:var(--muted)}
.card .go::before{content:"● ";color:var(--green)}

.pagetop{left:1010px;top:2572px;font-size:12px;color:var(--green-dark)}

/* footer */
.footer-line{left:0;top:2605px;width:1200px;border-top:3px solid var(--green)}
.foot-links{left:70px;top:2640px;display:grid;grid-template-columns:repeat(3,170px);row-gap:6px;font-size:12px;list-style:none}
.foot-links li:not(:empty)::before{content:"▸ ";color:var(--green)}
.foot-brand .brand-name{font-size:26px}
.foot-addr{left:820px;top:2720px;font-size:11px;line-height:1.8;color:var(--muted)}
.copy{left:0;top:2858px;width:1200px;text-align:center;font-size:11px;color:var(--muted)}
</style>
</head>
<body>

<header>
  <div class="abs brand">
    <div class="brand-mark"></div>
    <div><div class="brand-name">桜田クッキング</div><div class="brand-sub">SAKURADA Cooking School</div></div>
  </div>
  <div class="abs util"><span>会社概要</span><span>日本語版</span><span>English</span></div>
  <a class="abs reserve" href="#">体験レッスン予約はこちら</a>
  <nav class="abs gnav">
    <a class="active">ホーム<small>HOME</small></a>
    <a>桜田クッキングについて<small>ABOUT</small></a>
    <a>入会案内<small>JOIN US</small></a>
    <a>コース案内<small>COURSES</small></a>
    <a>料金表<small>PRICE</small></a>
    <a>よくある質問<small>FAQ</small></a>
    <a>教室案内<small>CLASSROOM</small></a>
  </nav>
</header>

<div class="abs hero" role="img" aria-label="料理をする手元と新鮮な野菜の写真"></div>
<div class="abs hero-veg" role="img" aria-label="トマトやパプリカなど色とりどりの野菜"></div>
<div class="abs hero-copy">
  <h1>実践こそが上達の近道！</h1>
  <p>一人ひとりの目線に合わせた<br>丁寧な指導で、料理の楽しさを<br>基礎からしっかり身につけます。</p>
</div>
<a class="abs hero-more" href="#">詳しく見る</a>
<div class="abs dots"><i></i><i></i><i></i></div>

<aside>
  <div class="abs trial">
    <svg class="trial-icon" viewBox="0 0 60 40"><path d="M10 30 Q30 5 50 30 Z" fill="none" stroke="#78b534" stroke-width="3"/><line x1="6" y1="32" x2="54" y2="32" stroke="#78b534" stroke-width="3"/></svg>
    <h2>見学・<br>体験レッスン</h2>
    <div class="badge">受付中!</div>
    <p class="lead">各教室にお電話ください</p>
    <div class="tel"><b>本校</b><span>03-5550-2638</span></div>
    <div class="tel"><b>日本橋</b><span>03-5550-0586</span></div>
    <div class="tel"><b>柏</b><span>04-5550-8587</span></div>
  </div>
  <ul class="abs side-nav">
    <li>HOME</li><li>桜田クッキングについて</li><li>入会案内</li><li>コース案内</li><li>料金表</li><li>よくある質問</li><li>教室案内</li><li>お問い合わせ</li>
  </ul>
  <div class="abs corp">
    <h3>企業のみなさまへ</h3>
    <p>社内イベント・料理講座等の<br>ご相談も承っております。</p>
  </div>
</aside>

<section class="abs news">
  <div class="sec-head"><h2>What's new</h2><small>新着情報のお知らせ</small></div>
  <div class="news-item"><div><time>2014年2月7日</time><br><span class="new">NEW</span></div>
    <p>ミトムアイドル【教室・日本橋校】 体験レッスン日程（費用：2,150円）<br>1月〜11月「春の献立」、他<br>1月〜12月「和食の基本」、他<br>1月〜29日「パスタ」、他</p></div>
  <div class="news-item"><div><time>2014年2月6日</time><br><span class="new">NEW</span></div>
    <p>【柏校】 フランス料理 2月16日 09:00〜15:00開催<br>親しい人を招いてのおもてなし料理です。<br>ご予約はお早めにお電話にてどうぞ。</p></div>
</section>

<section class="abs menu">
  <div class="sec-head"><h2 class="jp">今月のメニュー紹介</h2></div>
  <div class="menu-item"><div class="photo" role="img" aria-label="色鮮やかな前菜の料理写真" style="background:linear-gradient(135deg,#e6c25a,#c8582f 60%,#7fa63c)"></div>
    <div><h3>2014年2月<span>本格派</span> 前菜とグリーンサラダ</h3><p>季節の野菜をたっぷり使った前菜です。<br>ドレッシングの作り方も丁寧に学べます。</p></div></div>
  <div class="menu-item"><div class="photo" role="img" aria-label="スープ料理の写真" style="background:linear-gradient(135deg,#f2ead6,#d9b98a 60%,#a98a5a)"></div>
    <div><h3>2014年2月<span>基礎</span> 季節の野菜のポタージュ</h3><p>寒い日にぴったりのやさしいスープ。<br>素材の甘みを引き出すコツを覚えましょう。</p></div></div>
  <div class="menu-item"><div class="photo" role="img" aria-label="パスタ料理の写真" style="background:linear-gradient(135deg,#f0e0b8,#e0a24a 55%,#b8462c)"></div>
    <div><h3>2014年2月<span>イタリア</span> 手打ちパスタ</h3><p>生地から作る本格的なパスタです。<br>ソースとの合わせ方も紹介します。</p></div></div>
  <a class="more" href="#">一覧を見る</a>
</section>

<section class="abs about">
  <div class="about-title"><h2>SAKURADAクッキングについて</h2></div>
  <p class="about-lead">家庭で出来るフランス料理・和食を中心に幅広いコースをご用意しています</p>
  <div class="cards">
    <div class="card"><div class="photo" role="img" aria-label="教室で料理を学ぶ様子" style="background:linear-gradient(135deg,#c9b190,#7b5a3c)"></div><div class="card-body"><h3>桜田クッキングの特徴</h3><p>一人ひとりに寄り添う少人数制で、基礎から丁寧に指導します。</p><span class="go">詳しく見る</span></div></div>
    <div class="card"><div class="photo" role="img" aria-label="調理中の鍋の写真" style="background:linear-gradient(135deg,#b07a48,#4b3323)"></div><div class="card-body"><h3>レギュラーコース</h3><p>毎月の献立で家庭料理の基本を無理なく身につけます。</p><span class="go">詳しく見る</span></div></div>
    <div class="card"><div class="photo" role="img" aria-label="和食の盛り付け写真" style="background:linear-gradient(135deg,#ece4d4,#9a6a44)"></div><div class="card-body"><h3>専門・特別コース</h3><p>和食やフランス料理などを専門的に深く学べます。</p><span class="go">詳しく見る</span></div></div>
    <div class="card"><div class="photo" role="img" aria-label="肉料理の写真" style="background:linear-gradient(135deg,#d8a07a,#8c3f2a)"></div><div class="card-body"><h3>短期集中コース</h3><p>短い期間で必要な技術を集中して習得できます。</p><span class="go">詳しく見る</span></div></div>
    <div class="card"><div class="photo" role="img" aria-label="前菜の盛り合わせ写真" style="background:linear-gradient(135deg,#efe6cf,#c88b4a)"></div><div class="card-body"><h3>サンデーコース</h3><p>お忙しい方も日曜日に気軽に通えるコースです。</p><span class="go">詳しく見る</span></div></div>
    <div class="card"><div class="photo" role="img" aria-label="パンと料理の写真" style="background:linear-gradient(135deg,#f1e3c2,#b9823e)"></div><div class="card-body"><h3>料理コース</h3><p>おもてなしに役立つ一品を楽しく学びます。</p><span class="go">詳しく見る</span></div></div>
  </div>
</section>

<a class="abs pagetop" href="#">▲ ページトップへ</a>

<footer>
  <div class="abs footer-line"></div>
  <ul class="abs foot-links">
    <li>HOME</li><li>プライバシーポリシー</li><li>お問い合わせ</li>
    <li>桜田クッキングについて</li><li>会社概要</li><li>サイトマップ</li>
    <li>入会案内</li><li>料金表</li><li></li>
    <li>コース案内</li><li>教室案内</li><li></li>
    <li>よくある質問</li>
  </ul>
  <div class="abs foot-brand brand" style="left:820px;top:2640px">
    <div class="brand-mark" style="width:38px;height:38px"></div>
    <div><div class="brand-name">桜田クッキング</div><div class="brand-sub">SAKURADA Cooking School</div></div>
  </div>
  <p class="abs foot-addr">■本校 東京都中央区桜田1-2-3 TEL 03-5550-2638<br>■日本橋校 東京都中央区桜田4-5-6 TEL 03-5550-0586<br>■柏校 千葉県柏市桜田7-8-9 TEL 04-5550-8587</p>
  <p class="abs copy">Copyright © 2014 SAKURADA Cooking School All Rights Reserved.</p>
</footer>

</body>
</html>
```